Pelling Home Efficiency

Id like for my business card to be very bold and professional. Incorporating the business logo, the main services offered, and my contact info. Services are spray foam, insulation, new construction, retrofit, weatherization.

When opening this project art huddle was not able to upload my new logo that I picked from another recent art huddle project. Does anyone know how i could upload my logo onto the page for design of the business cards?

Target Market(s)

Building owners, contractors

Industry/Entity Type

Building Insulation and performance improvements

Contact Information for Business Card

Owner, Email marcus@pellinghomeefficiency.com Phone number 555-204-6817

Colors
0054AA
0677BA
7BADD7
CADEEF
E8F1F8
F0912C
F2A743
F7CA91
FBE8D2
FDF5EE

Requirements
Must have
• Services- spray foam, cellulose, mineral wool, fiberglass, air sealing, new construction, retrofit, weatherization, energy saving assesments

```html
<!DOCTYPE html>
<html lang="en">
<head>
<meta charset="utf-8">
<title>Pelling Home Efficiency – Business Cards</title>
<link rel="stylesheet" href="https://fonts.googleapis.com/css2?family=Open+Sans:wght@400;600;700&display=swap">
<style>
  :root {
    --blue-deep: #0054AA;
    --blue: #0677BA;
    --blue-bright: #2BA3DC;
    --blue-soft: #7BADD7;
    --orange: #E0711C;
    --orange-soft: #F0912C;
    --peach: #FBE8D2;
    --ink: #333a40;
    --card-white: #ffffff;
    --card-shade: #e6e6e6;
    --backdrop: #2e2f31;
  }
  * { box-sizing: border-box; margin: 0; padding: 0; }
  html, body { width: 1200px; height: 900px; overflow: hidden; }
  body {
    background: var(--backdrop);
    font-family: "Open Sans", Arial, sans-serif;
    display: flex;
    flex-direction: column;
    align-items: center;
    justify-content: center;
    gap: 40px;
  }
  .card {
    position: relative;
    width: 700px;
    height: 400px;
    background: linear-gradient(100deg, var(--card-white) 0%, var(--card-shade) 48%, var(--card-white) 100%);
    box-shadow: 0 10px 26px rgba(0,0,0,.45);
    overflow: hidden;
  }
  .brand {
    position: absolute;
    top: 70px;
    left: 330px;
    display: flex;
    align-items: center;
    gap: 12px;
  }
  .brand-mark {
    width: 18px;
    height: 18px;
    background: var(--blue-bright);
  }
  .brand-name {
    color: var(--orange);
    font-weight: 700;
    font-size: 26px;
    letter-spacing: .2px;
  }
  .rule-heading {
    position: absolute;
    left: 60px;
    right: 60px;
    display: flex;
    align-items: baseline;
    gap: 10px;
    font-weight: 700;
    color: var(--orange);
    text-transform: uppercase;
  }
  .rule-heading::after {
    content: "";
    flex: 1;
    height: 1px;
    transform: translateY(-6px);
  }
  .services-title { top: 250px; font-size: 18px; }
  .services-title::after { background: var(--orange-soft); }
  .services-list {
    position: absolute;
    left: 72px;
    top: 284px;
    right: 40px;
    list-style: none;
    color: var(--ink);
    font-size: 16.5px;
    line-height: 1.65;
  }
  .services-list li { display: flex; flex-wrap: wrap; gap: 0 8px; }
  .services-list span::before {
    content: "";
    display: inline-block;
    width: 6px;
    height: 6px;
    background: var(--blue-bright);
    margin-right: 6px;
    vertical-align: middle;
  }
  .contact-name { top: 255px; font-size: 19px; }
  .contact-name::after { background: var(--blue-soft); transform: translateY(8px); }
  .contact-role {
    position: absolute;
    left: 70px;
    top: 280px;
    color: var(--blue-bright);
    font-size: 17px;
  }
  .contact-lines {
    position: absolute;
    left: 80px;
    top: 315px;
    list-style: none;
    color: var(--ink);
    font-size: 16.5px;
    line-height: 1.8;
  }
  .contact-lines li { display: flex; align-items: center; gap: 10px; }
  .contact-lines svg { width: 16px; height: 16px; fill: var(--orange); }
</style>
</head>
<body>

  <section class="card card-front" aria-label="Card front – services">
    <div class="brand">
      <span class="brand-mark"></span>
      <span class="brand-name">Pelling Home Efficiency</span>
    </div>
    <h2 class="rule-heading services-title">Services</h2>
    <ul class="services-list">
      <li><span>Spray Foam</span><span>Cellulose</span><span>Mineral Wool</span><span>Fiberglass</span><span>Air Sealing</span></li>
      <li><span>New Construction</span><span>Retrofit</span><span>Weatherization</span><span>Energy Saving Assesments</span></li>
    </ul>
  </section>

  <section class="card card-back" aria-label="Card back – contact">
    <div class="brand">
      <span class="brand-mark"></span>
      <span class="brand-name">Pelling Home Efficiency</span>
    </div>
    <h2 class="rule-heading contact-name">Marcus</h2>
    <p class="contact-role">Owner</p>
    <ul class="contact-lines">
      <li>
        <svg viewBox="0 0 24 24" aria-hidden="true"><path d="M6.6 10.8a15.1 15.1 0 0 0 6.6 6.6l2.2-2.2c.3-.3.7-.4 1-.2 1.1.4 2.3.6 3.6.6.6 0 1 .4 1 1V20c0 .6-.4 1-1 1A17 17 0 0 1 3 4c0-.6.4-1 1-1h3.5c.6 0 1 .4 1 1 0 1.3.2 2.5.6 3.6.1.3 0 .7-.2 1z"/></svg>
        555-204-6817
      </li>
      <li>
        <svg viewBox="0 0 24 24" aria-hidden="true"><path d="M2 5h20v14H2zm2 2v.4l8 5 8-5V7zm0 2.8V17h16V9.8l-8 5z"/></svg>
        marcus@pellinghomeefficiency.com
      </li>
    </ul>
  </section>

</body>
</html>
```